Infographic & Data Visualisation Design for – Australia’s Yearly Harmwatch Review 2026

About Carrowby Institute: Carrowby Institute is an independent non-profit public health organization. We produce Australia’s Yearly Harmwatch Review, which translates verified national mortality data into actionable insights for policymakers, journalists, healthcare workers, and the general public.

Project Goal: We need a suite of high-impact, clean, and authoritative infographics and data visualisations created for Australia’s Yearly Harmwatch Review 2026.

What We Are Providing:

Full Dataset (.xlsx): Complete Excel file containing all 2026 report data.

Data & Chart Guidance Doc (.docx): A summary document detailing each dataset, the core takeaway, and our initial recommendations for chart types (e.g., line graphs, horizontal bar charts, donut charts, metric tiles).

Carrowby Institute Brand Book (.pdf): Complete brand guidelines covering fonts, colors, line weights, and imagery. These guidelines and in particular colours should be used across the infographics.

Previous Year Reference: You can view how last year’s report and graphics here: https://www.carrowby-example.org.au/australias-yearly-harmwatch-review-2025/

Designer Input & Creative Freedom: While we have provided a guide suggesting specific chart types for each dataset, we are not data visualisation experts - you are! We are very open to your creative ideas, structural suggestions, and design expertise. If you identify a clearer, more engaging, or visually compelling way to illustrate a specific dataset, we welcome your input.

Required Deliverables:

Master Report Infographics: High-resolution, print/PDF-ready A4 vector graphics for the formal report publication (Delivered as vector AI/EPS and high-res PDF/PNG).

Web Assets: Web-optimized PNG/SVG files with transparent or brand backgrounds.

Social Media Adaptations: 1:1 (Square) and 4:5 / 9:16 (Vertical) graphic cards for Pictoral, WorkMesh, Chatterly, and X.
Updates

Deadline was too tight - have extended it to ensure the designers have enough time to do the job.

Target Market(s)

Policy makers, journalists, health sector professionals, frontline workers, and the general public.

Industry/Entity Type

Drug/Government/Not for Profit

Font styles to use
Sans Serif
Other font styles liked:
• Brand Fonts: Use any or a combination of: Host Grotesk or Libre Baskerville or Poppins or Calibri Light

Colors

Designer to choose colors to be used in the design.

Requirements
Must have
• The ability to create Infographics, graphs of all kinds from data that we have given.
Nice to have
• Help with choosing what infographics/graphs/donuts graphs etc will be best to visualise the data.
Should not have
• A designer who has not made graphs or infographics from Data.

```html
<!DOCTYPE html>
<html lang="en">
<head>
<meta charset="utf-8">
<title>Australia’s Yearly Harmwatch Review 2026 – Carrowby Institute</title>
<link href="https://fonts.googleapis.com/css2?family=Barlow+Semi+Condensed:wght@600;700;800&family=Barlow:wght@400;500;600;700&display=swap" rel="stylesheet">
<style>
  :root{
    --teal:#1b7f7a;
    --teal-mid:#3aa6a0;
    --teal-soft:#a9d9d6;
    --teal-pale:#eaf5f4;
    --navy:#0f2a47;
    --ink:#1d2a3a;
    --purple:#5b3a8c;
    --lavender:#f2eff8;
    --line:#d9e6e5;
    --white:#ffffff;
  }
  *{box-sizing:border-box;margin:0;padding:0}
  html,body{width:800px;height:1200px;overflow:hidden;background:var(--white)}
  body{font-family:"Barlow",Arial,sans-serif;color:var(--ink)}
  .canvas{position:relative;width:800px;height:1200px;overflow:hidden;background:var(--white)}
  .abs{position:absolute}

  .side-band{left:0;top:0;width:31px;height:1155px;background:linear-gradient(180deg,#d7eeec 0%,#eef7f6 60%,#f6fbfa 100%)}
  .side-band span{position:absolute;left:8px;top:300px;transform:rotate(-90deg);transform-origin:left top;white-space:nowrap;font-size:9.5px;font-weight:600;letter-spacing:.9px;color:var(--navy)}

  .brand{left:57px;top:32px;display:flex;align-items:center;gap:10px}
  .brand-mark{width:36px;height:36px;border:2px solid var(--teal);border-radius:50%}
  .brand-name{font-family:"Barlow",sans-serif;font-weight:600;font-size:15px;line-height:17px;letter-spacing:.6px;color:var(--navy);text-transform:uppercase}

  .title{left:209px;top:22px;width:460px;font-family:"Barlow Semi Condensed",sans-serif;font-weight:800;font-size:41px;line-height:44px;color:var(--navy);text-transform:uppercase}
  .title-rule{left:209px;top:122px;width:73px;height:2px;background:var(--teal-mid)}
  .subtitle{left:209px;top:137px;width:420px;font-size:13px;line-height:19px;color:var(--ink)}

  .pillars{left:667px;top:28px;width:1px;height:130px;background:var(--line)}
  .pillar{left:688px;display:flex;align-items:center;gap:12px}
  .pillar svg{width:26px;height:26px;flex:none}
  .pillar span{font-size:10.5px;font-weight:600;line-height:13px;color:var(--navy);text-transform:uppercase;letter-spacing:.3px}

  .hero-icon{left:108px;top:206px;width:104px;height:104px;border:2px solid var(--teal);border-radius:50%;background:var(--white)}
  .hero-number{left:232px;top:170px;font-family:"Barlow Semi Condensed",sans-serif;font-weight:800;font-size:208px;line-height:200px;color:var(--teal);letter-spacing:-4px}
  .hero-caption{left:0;top:353px;width:800px;text-align:center;font-family:"Barlow Semi Condensed",sans-serif;font-weight:700;font-size:27px;color:var(--navy)}
  .hero-caption em{font-style:normal;color:var(--teal)}

  .data-label{left:116px;top:400px;width:594px;display:flex;align-items:center;gap:16px}
  .data-label i{flex:1;height:1px;background:var(--teal-mid)}
  .data-label span{font-size:12px;font-weight:500;letter-spacing:1px;color:var(--navy)}

  .stat-card{top:432px;height:100px;border-radius:8px;background:var(--teal-pale);display:flex;align-items:center}
  .stat-card.is-day{background:var(--lavender)}
  .stat-card svg{position:absolute;left:22px;top:20px;width:60px;height:60px}
  .stat-text{position:absolute;left:0;right:0;top:14px;text-align:center}
  .stat-when{font-size:12.5px;font-weight:500;letter-spacing:.4px;color:var(--navy)}
  .stat-value{font-family:"Barlow Semi Condensed",sans-serif;font-weight:800;font-size:46px;line-height:46px;color:var(--teal)}
  .is-day .stat-value{color:var(--purple)}
  .stat-unit{font-size:12.5px;font-weight:500;letter-spacing:.6px;color:var(--navy)}

  .map-intro{left:54px;top:580px;width:120px}
  .map-intro h2{font-family:"Barlow Semi Condensed",sans-serif;font-weight:700;font-size:15px;line-height:17px;color:var(--navy);text-transform:uppercase}
  .map-intro i{display:block;width:38px;height:2px;background:var(--teal-mid);margin:8px 0 14px}
  .map-intro p{font-size:11px;line-height:16.5px;color:var(--ink);margin-bottom:9px}

  .map-area{left:282px;top:556px;width:342px;height:316px;border-radius:46px 60px 40px 80px;background:linear-gradient(135deg,#e4f2f1 0%,#bfe2df 55%,#3f9f99 100%)}
  .leaders{left:0;top:0;width:800px;height:1200px;pointer-events:none}

  .region{text-align:left}
  .region b{display:block;font-size:9px;font-weight:600;letter-spacing:.2px;line-height:11px;color:var(--navy);text-transform:uppercase}
  .region span{display:block;font-family:"Barlow Semi Condensed",sans-serif;font-weight:700;font-size:23px;line-height:26px;color:var(--teal)}

  .substances{left:38px;top:882px;width:324px;height:246px;border:1px solid var(--line);border-radius:8px;background:var(--white);padding:20px 12px 0 12px}
  .substances h2{font-family:"Barlow Semi Condensed",sans-serif;font-weight:700;font-size:14px;line-height:17px;color:var(--navy);text-transform:uppercase}
  .substances .rule{width:35px;height:2px;background:var(--teal-mid);margin:6px 0 8px}
  .sub-row{display:flex;align-items:center;height:32.5px;border-bottom:1px solid var(--line);margin-left:0;width:304px}
  .sub-row:last-child{border-bottom:none}
  .sub-rank{width:20px;height:20px;border-radius:50%;background:var(--teal);color:var(--white);font-size:11px;font-weight:600;display:flex;align-items:center;justify-content:center;flex:none}
  .sub-icon{width:29px;height:29px;border-radius:50%;background:var(--teal);margin-left:13px;flex:none;display:flex;align-items:center;justify-content:center}
  .sub-icon svg{width:17px;height:17px}
  .sub-name{margin-left:13px;flex:1;font-size:12px;font-weight:500;color:var(--navy)}
  .sub-count{font-size:13px;font-weight:600;color:var(--navy);width:36px;text-align:right}

  .insight{left:375px;top:895px;width:382px;height:231px;border-radius:10px;background:var(--teal-pale);padding:22px 0 0 16px}
  .insight-head{display:flex;align-items:center;gap:14px}
  .insight-head svg{width:36px;height:26px}
  .insight-head span{font-family:"Barlow Semi Condensed",sans-serif;font-weight:700;font-size:15px;color:var(--teal);letter-spacing:.3px}
  .insight h3{margin-top:12px;width:220px;font-family:"Barlow Semi Condensed",sans-serif;font-weight:700;font-size:19px;line-height:24px;color:var(--navy)}
  .insight .rule{width:205px;height:1px;background:var(--teal-mid);margin:13px 0 12px}
  .insight p{width:210px;font-size:10.5px;line-height:16px;color:var(--ink)}
  .insight-art{left:240px;top:50px;width:124px;height:122px;border-radius:50%;background:radial-gradient(circle,#d3ecea 0%,#eaf5f4 75%)}

  .source{left:38px;top:1132px;font-size:8px;color:var(--ink)}
  .source b{font-weight:700}

  .footer{left:0;top:1155px;width:800px;height:45px;background:var(--navy);display:flex;align-items:center;padding:0 32px;color:var(--white)}
  .footer-brand{display:flex;align-items:center;gap:9px;font-size:11.5px;font-weight:500;letter-spacing:.5px;text-transform:uppercase}
  .footer-brand i{width:20px;height:20px;border:1.5px solid var(--teal-soft);border-radius:50%}
  .footer-sep{width:1px;height:22px;background:#56708c;margin:0 12px}
  .footer-url{font-size:9px}
  .footer-copy{margin-left:auto;font-size:9px}
</style>
</head>
<body>
<main class="canvas">

  <div class="abs side-band"><span>INDEPENDENT. EVIDENCE-BASED. ACTION-FOCUSED.</span></div>

  <div class="abs brand">
    <i class="brand-mark"></i>
    <div class="brand-name">Carrowby<br>Institute</div>
  </div>

  <h1 class="abs title">Australia’s Yearly<br>Harmwatch Review 2026</h1>
  <div class="abs title-rule"></div>
  <p class="abs subtitle">Drug-induced deaths remain one of Australia’s most significant preventable public health challenges.</p>

  <div class="abs pillars"></div>
  <div class="abs pillar" style="top:30px">
    <svg viewBox="0 0 26 26"><path d="M13 2 L23 6 V13 C23 19 18 23 13 25 C8 23 3 19 3 13 V6 Z" fill="var(--navy)"/><path d="M8 13 L12 17 L18 9" stroke="#fff" stroke-width="2.4" fill="none"/></svg>
    <span>Evidence<br>Based</span>
  </div>
  <div class="abs pillar" style="top:76px">
    <svg viewBox="0 0 26 26"><rect x="3" y="14" width="5" height="10" fill="var(--teal)"/><rect x="10.5" y="9" width="5" height="15" fill="var(--navy)"/><rect x="18" y="3" width="5" height="21" fill="var(--teal)"/></svg>
    <span>Data<br>Driven</span>
  </div>
  <div class="abs pillar" style="top:122px">
    <svg viewBox="0 0 26 26"><circle cx="13" cy="13" r="11" fill="var(--navy)"/></svg>
    <span>Action<br>Focused</span>
  </div>

  <div class="abs hero-icon" role="img" aria-label="Group of people icon"></div>
  <div class="abs hero-number">2,596</div>
  <p class="abs hero-caption">Australians lost their lives to <em>drug-induced</em> causes</p>

  <div class="abs data-label"><i></i><span>2024 NATIONAL MORTALITY DATA</span><i></i></div>

  <div class="abs stat-card" style="left:64px;width:225px">
    <svg viewBox="0 0 60 60" fill="none" stroke="var(--teal)" stroke-width="2.5"><rect x="6" y="10" width="48" height="42" rx="4"/><line x1="6" y1="21" x2="54" y2="21"/><line x1="18" y1="5" x2="18" y2="15"/><line x1="42" y1="5" x2="42" y2="15"/><g fill="var(--teal)" stroke="none"><rect x="14" y="28" width="6" height="6"/><rect x="27" y="28" width="6" height="6"/><rect x="40" y="28" width="6" height="6"/><rect x="14" y="39" width="6" height="6"/><rect x="27" y="39" width="6" height="6"/><rect x="40" y="39" width="6" height="6"/></g></svg>
    <div class="stat-text" style="left:60px"><div class="stat-when">EVERY WEEK</div><div class="stat-value">50</div><div class="stat-unit">DEATHS</div></div>
  </div>
  <div class="abs stat-card is-day" style="left:304px;width:216px">
    <svg viewBox="0 0 60 60" fill="none" stroke="var(--purple)" stroke-width="2.5"><circle cx="30" cy="30" r="25"/><path d="M30 14 V30 L40 38"/></svg>
    <div class="stat-text" style="left:60px"><div class="stat-when">EVERY DAY</div><div class="stat-value">7</div><div class="stat-unit">DEATHS</div></div>
  </div>
  <div class="abs stat-card" style="left:536px;width:221px">
    <svg viewBox="0 0 60 60" fill="none" stroke="var(--teal)" stroke-width="2.5"><circle cx="30" cy="33" r="22"/><rect x="25" y="4" width="10" height="6"/><line x1="30" y1="10" x2="30" y2="11"/><line x1="47" y1="14" x2="51" y2="10"/><path d="M30 20 V33 H40"/></svg>
    <div class="stat-text" style="left:60px"><div class="stat-when">EVERY 3.5 HOURS</div><div class="stat-value">1</div><div class="stat-unit">DEATH</div></div>
  </div>

  <div class="abs map-intro">
    <h2>Deaths by State<br>&amp; Territory</h2>
    <i></i>
    <p>Drug-induced deaths occur in every part of Australia.</p>
    <p>Numbers include all drug-induced deaths (2024).</p>
  </div>

  <div class="abs map-area" role="img" aria-label="Map of Australia shaded by state and territory, darker teal for higher drug-induced death counts"></div>

  <svg class="abs leaders" viewBox="0 0 800 1200" fill="none" stroke="var(--navy)" stroke-width="0.8">
    <line x1="398" y1="600" x2="413" y2="642"/><circle cx="413" cy="642" r="1.8" fill="var(--navy)"/>
    <polyline points="617,624 580,624 564,671"/><circle cx="564" cy="671" r="1.8" fill="var(--navy)"/>
    <polyline points="246,682 276,682 305,710"/><circle cx="305" cy="710" r="1.8" fill="var(--navy)"/>
    <polyline points="673,712 608,712 588,730"/><circle cx="588" cy="730" r="1.8" fill="var(--navy)"/>
    <line x1="675" y1="772" x2="572" y2="775"/><circle cx="572" cy="776" r="2.5" fill="#fff"/>
    <polyline points="332,794 362,794 412,752"/><circle cx="412" cy="752" r="1.8" fill="var(--navy)"/>
    <polyline points="620,828 594,828 575,805 550,803"/><circle cx="550" cy="803" r="1.8" fill="var(--navy)"/>
    <line x1="474" y1="852" x2="542" y2="855"/><circle cx="542" cy="855" r="1.8" fill="var(--navy)"/>
  </svg>

  <div class="abs region" style="left:346px;top:556px"><b>Northern Territory</b><span style="padding-left:42px">15</span></div>
  <div class="abs region" style="left:623px;top:602px"><b>Queensland</b><span style="padding-left:14px">417</span></div>
  <div class="abs region" style="left:193px;top:650px"><b>Western<br>Australia</b><span style="margin-left:7px">278</span></div>
  <div class="abs region" style="left:653px;top:690px"><b>New South Wales</b><span style="padding-left:22px">587</span></div>
  <div class="abs region" style="left:655px;top:743px;text-align:center"><b>Australian Capital<br>Territory</b><span>29</span></div>
  <div class="abs region" style="left:238px;top:790px"><b>South Australia</b><span style="padding-left:16px">157</span></div>
  <div class="abs region" style="left:628px;top:811px"><b>Victoria</b><span>572</span></div>
  <div class="abs region" style="left:428px;top:836px"><b>Tasmania</b><span style="padding-left:10px">35</span></div>

  <section class="abs substances">
    <h2>Leading substances involved in<br>unintentional overdose deaths (2024)</h2>
    <div class="rule"></div>
    <div class="sub-row">
      <span class="sub-rank">1</span>
      <span class="sub-icon"><svg viewBox="0 0 17 17" fill="none" stroke="#fff" stroke-width="1.5"><rect x="2" y="5.5" width="13" height="6" rx="3" transform="rotate(-45 8.5 8.5)"/><line x1="6.4" y1="6.4" x2="10.6" y2="10.6"/></svg></span>
      <span class="sub-name">Opioids</span><span class="sub-count">877</span>
    </div>
    <div class="sub-row">
      <span class="sub-rank">2</span>
      <span class="sub-icon"><svg viewBox="0 0 17 17" fill="none" stroke="#fff" stroke-width="1.5"><path d="M8.5 1.5 L14 8.5 L8.5 15.5 L3 8.5 Z"/><line x1="8.5" y1="1.5" x2="8.5" y2="15.5"/></svg></span>
      <span class="sub-name">Amphetamine-type stimulants</span><span class="sub-count">772</span>
    </div>
    <div class="sub-row">
      <span class="sub-rank">3</span>
      <span class="sub-icon"><svg viewBox="0 0 17 17" fill="none" stroke="#fff" stroke-width="1.5"><circle cx="8.5" cy="8.5" r="6"/><line x1="4.5" y1="12.5" x2="12.5" y2="4.5"/></svg></span>
      <span class="sub-name">Benzodiazepines</span><span class="sub-count">514</span>
    </div>
    <div class="sub-row">
      <span class="sub-rank">4</span>
      <span class="sub-icon"><svg viewBox="0 0 17 17" fill="none" stroke="#fff" stroke-width="1.5"><rect x="7" y="1.5" width="3" height="3"/><rect x="5" y="4.5" width="7" height="11" rx="1.5"/><line x1="5" y1="9" x2="12" y2="9"/></svg></span>
      <span class="sub-name">Alcohol</span><span class="sub-count">311</span>
    </div>
    <div class="sub-row">
      <span class="sub-rank">5</span>
      <span class="sub-icon"><svg viewBox="0 0 17 17"><circle cx="8.5" cy="8.5" r="5" fill="none" stroke="#fff" stroke-width="1.5"/></svg></span>
      <span class="sub-name">Antidepressants</span><span class="sub-count">293</span>
    </div>
  </section>

  <section class="abs insight">
    <div class="insight-head">
      <svg viewBox="0 0 36 26" fill="var(--teal)"><path d="M0 26 V15 C0 6 5 1 13 0 V5 C8 6 6 9 6 13 H14 V26 Z"/><path d="M20 26 V15 C20 6 25 1 33 0 V5 C28 6 26 9 26 13 H34 V26 Z"/></svg>
      <span>KEY INSIGHT</span>
    </div>
    <h3>More Australians die from drug-induced causes than many people realise.</h3>
    <div class="rule"></div>
    <p>The burden is experienced across every state and territory, highlighting the need for evidence-based prevention, treatment and harm reduction responses.</p>
    <div class="abs insight-art" role="img" aria-label="Line illustration of open hands holding a small group of people"></div>
  </section>

  <p class="abs source"><b>Source:</b> NSA National Mortality Database (2024).</p>

  <footer class="abs footer">
    <div class="footer-brand"><i></i>Carrowby Institute</div>
    <span class="footer-sep"></span>
    <span class="footer-url">carrowby-example.org.au</span>
    <span class="footer-copy">© Carrowby Institute 2026</span>
  </footer>

</main>
</body>
</html>
```